10 mail templates for erotic datig site

We need to do 10 mail templates to send for non registered users. Mail campaign will be focused to make a registration. It will be good to do 7 templates focused on man and 1 focused on woman and 2 unisex templates. On the template for women you can write: free full membership or everything is for free, read our sex magazine, find sex partner today etc. On the template for man you can write: free registration, verified profiles, sex magazine, erotic stories, sex today - no problem, find your affair, find your sex partner for tonight etc. Don't use porno photos or photos with complete nudity. Please use nice sexy photos. You can check our site here: www.lumavexo.cz

```html
<!DOCTYPE html>
<html lang="en">
<head>
<meta charset="utf-8">
<title>lumavexo.cz – registration mail</title>
<link rel="stylesheet" href="https://fonts.googleapis.com/css2?family=Arimo:wght@400;700&family=Open+Sans:wght@700&family=Noto+Sans:wght@400&display=swap">
<style>
  :root {
    --red: #ff0000;
    --red-deep: #d60000;
    --white: #ffffff;
    --ink: #111111;
    --grey-light: #cbcbcb;
    --grey-mid: #9e9e9e;
    --black-band: #1c1c1c;
    --shadow: #4a4a4a;
    --photo-warm: #c98a6a;
  }
  html, body {
    margin: 0;
    padding: 0;
    width: 1200px;
    height: 2476px;
    overflow: hidden;
    background: var(--white);
  }
  .canvas {
    position: relative;
    width: 1200px;
    height: 2476px;
    font-family: "Arimo", Arial, sans-serif;
    color: var(--ink);
  }
  .glow-top {
    position: absolute;
    left: 92px; top: 72px;
    width: 1040px; height: 190px;
    background: var(--red);
    border-radius: 60px;
    filter: blur(16px);
  }
  .glow-bottom {
    position: absolute;
    left: 104px; top: 2210px;
    width: 1028px; height: 160px;
    background: var(--shadow);
    border-radius: 60px;
    filter: blur(22px);
    opacity: .9;
  }
  .mail {
    position: absolute;
    left: 79px; top: 275px;
    width: 1063px; height: 1900px;
  }
  .section { position: absolute; left: 0; width: 1063px; }
  .header { top: 0; height: 389px; background: var(--red); }
  .intro { top: 389px; height: 563px; background: var(--grey-light); }
  .community { top: 952px; height: 643px; background: var(--black-band); color: var(--white); }
  .story { top: 1595px; height: 305px; background: var(--grey-mid); }

  .brand {
    position: absolute;
    left: 6px; top: 8px;
    margin: 0;
    font-weight: 400;
    font-size: 100px;
    line-height: 1;
    color: var(--white);
    letter-spacing: -1px;
  }
  .tagline {
    position: absolute;
    left: 43px; top: 181px;
    width: 499px; height: 73px;
    background: var(--red-deep);
    border-radius: 3px;
    color: var(--white);
    font-size: 29px;
    line-height: 73px;
    text-align: center;
  }
  .photo {
    position: absolute;
    background: linear-gradient(135deg, #a86a52, var(--photo-warm) 55%, #8a4c3c);
  }
  .photo-couple { left: 741px; top: 114px; width: 291px; height: 229px; }
  .photo-garden {
    left: 22px; top: 301px; width: 202px; height: 303px;
    background: linear-gradient(160deg, #6f8a4d, #d98fb0 55%, #8fb0c8);
  }
  .photo-lingerie {
    left: 820px; top: 1px; width: 207px; height: 300px;
    background: linear-gradient(160deg, #e9d6c7, #d8a98e 50%, #b0242c);
  }

  .pitch {
    position: absolute;
    left: 42px;
    margin: 0;
    font-size: 36px;
    line-height: 1;
    white-space: nowrap;
  }
  .pitch b { font-weight: 700; }

  .button {
    position: absolute;
    width: 302px; height: 71px;
    background: var(--red);
    border-radius: 14px;
    color: var(--white);
    font-family: "Open Sans", Arial, sans-serif;
    font-weight: 700;
    font-size: 47px;
    line-height: 68px;
    text-align: center;
    text-decoration: none;
  }
  .offer {
    position: absolute;
    left: 361px; top: 493px;
    font-family: "Noto Sans", Arial, sans-serif;
    font-size: 58px;
    line-height: 1;
    color: var(--ink);
  }
  .now {
    position: absolute;
    left: 811px; top: 480px;
    font-size: 74px;
    line-height: 1;
    color: var(--red);
    -webkit-text-stroke: 2px var(--white);
    paint-order: stroke fill;
  }

  .count {
    position: absolute;
    left: 0; top: 48px;
    width: 1063px;
    margin: 0;
    text-align: center;
    font-family: "Noto Sans", Arial, sans-serif;
    font-size: 55px;
    line-height: 72px;
  }
  .count strong { display: block; font-family: "Arimo", Arial, sans-serif; font-weight: 700; }
  .perk {
    position: absolute;
    right: 53px; top: 410px;
    margin: 0;
    text-align: right;
    font-family: "Noto Sans", Arial, sans-serif;
    font-size: 50px;
    line-height: 65px;
    letter-spacing: 2px;
  }

  .story-title {
    position: absolute;
    left: 38px; top: 96px;
    margin: 0;
    font-size: 74px;
    font-weight: 400;
    line-height: 1;
    color: var(--red);
    white-space: nowrap;
  }
  .story-title .kicker { color: var(--white); font-weight: 700; }
</style>
</head>
<body>
<div class="canvas">
  <div class="glow-top"></div>
  <div class="glow-bottom"></div>

  <main class="mail">
    <header class="section header">
      <h1 class="brand">lumavexo.cz</h1>
      <div class="tagline">The best erotic dating site</div>
      <div class="photo photo-couple" role="img" aria-label="Photo of an embracing couple on a bed"></div>
    </header>

    <section class="section intro">
      <p class="pitch" style="top:42px">Bored of daily <b>routine</b>?.</p>
      <p class="pitch" style="top:141px">Tired of always repeating with <b>same partner</b>?.</p>
      <p class="pitch" style="top:241px"><b>Why not try something else</b>?.</p>
      <p class="pitch" style="top:338px">On <b>lumavexo.cz</b> you can get the best erotic sex dates.</p>
      <a class="button" href="#" style="left:29px; top:443px">join us</a>
      <span class="offer">free registration</span>
      <span class="now">NOW¡</span>
    </section>

    <section class="section community">
      <p class="count">More than<strong>830,000</strong>registered users &amp; verified profiles</p>
      <div class="photo photo-garden" role="img" aria-label="Photo of a smiling woman in a pink top sitting in a garden"></div>
      <a class="button" href="#" style="left:371px; top:295px">join us</a>
      <p class="perk">AND get total access<br>to best sex<br>magazine in Europe.</p>
    </section>

    <section class="section story">
      <h2 class="story-title"><span class="kicker">SEX</span> history of the day</h2>
      <a class="button" href="#" style="left:486px; top:210px">Read</a>
      <div class="photo photo-lingerie" role="img" aria-label="Photo of a woman in red lingerie"></div>
    </section>
  </main>
</div>
</body>
</html>
```